Retractable Banner Design featuring Key Product for Beauty Trade Show (Eyelash Extensions)

We're a beauty/nail supply company that specializes in products used in professional nail salons. The key product for this design is "Eyelash Extensions".

We will be exhibiting in a trade show and are looking for a free-standing Retractable Banner Design that will be displayed at the front of our booth. The goal of the banner will be to display key products that are high in demand with our customers. The banner will be used to attract attention and highlight key selling points of these popular products. We would like the banner to be focused on the product title, image and key points, with a beauty/model/pattern background to create a professional appearance.

Target Market(s)

Nail Salons

Industry/Entity Type

Beauty

Requirements
Nice to have
• Eyelash model or close up of eyelash product in use.

```html
<!DOCTYPE html>
<html lang="en">
<head>
<meta charset="utf-8">
<title>Velvet Lash – Eyelash Extensions Roll-Up Banner</title>
<link href="https://fonts.googleapis.com/css2?family=Montserrat:wght@500;700;800&display=swap" rel="stylesheet">
<style>
  :root {
    --coral: #f6545a;
    --ink: #111111;
    --white: #ffffff;
    --skin-light: #e3b69e;
    --skin-mid: #b9826a;
    --skin-dark: #5a3426;
    --tray-light: #f2f2f2;
    --tray-dark: #8d8d8d;
  }
  * { margin: 0; padding: 0; box-sizing: border-box; }
  html, body { width: 1200px; height: 4000px; overflow: hidden; background: var(--white); }
  body { font-family: "Montserrat", sans-serif; color: var(--ink); }
  .banner { position: relative; width: 1200px; height: 4000px; overflow: hidden; background: var(--white); }
  .layer { position: absolute; left: 0; top: 0; }

  .brand-name {
    position: absolute; top: 190px; left: 0; width: 100%;
    text-align: center; font-size: 96px; font-weight: 700; color: var(--ink);
  }
  .headline { position: absolute; top: 360px; left: 0; width: 100%; text-align: center; line-height: 1; }
  .headline .accent { display: block; color: var(--coral); font-size: 150px; font-weight: 800; }
  .headline .main { display: block; color: var(--ink); font-size: 150px; font-weight: 800; margin-top: 40px; letter-spacing: 2px; }

  .product-band { position: absolute; top: 2095px; left: 0; width: 1200px; height: 315px; background: var(--coral); }
  .product { position: absolute; top: 1900px; width: 334px; text-align: center; }
  .product-tile {
    height: 390px; border-radius: 40px; background: var(--white);
    padding: 16px; box-shadow: 0 4px 10px rgba(0,0,0,.15);
  }
  .product-shot {
    width: 100%; height: 100%; border-radius: 28px;
    background: linear-gradient(180deg, var(--tray-light) 0%, var(--tray-dark) 50%, var(--tray-light) 100%);
  }
  .product-name { margin-top: 28px; font-size: 36px; font-weight: 700; color: var(--ink); }

  .feature { position: absolute; left: 89px; width: 1030px; height: 150px; }
  .feature-icon { position: absolute; left: 0; top: 0; width: 150px; height: 150px; }
  .feature-text { position: absolute; left: 200px; top: 8px; }
  .feature-title { font-size: 42px; font-weight: 700; color: var(--coral); line-height: 1.15; }
  .feature-desc { font-size: 32px; font-weight: 500; color: var(--ink); line-height: 1.3; max-width: 780px; }

  .pack-info {
    position: absolute; top: 3780px; left: 0; width: 100%;
    display: flex; justify-content: center; gap: 70px;
    font-size: 64px; font-weight: 800; color: var(--white);
  }
  .pack-info .num { color: var(--coral); }
</style>
</head>
<body>
<main class="banner">

  <!-- hero photo + swoosh -->
  <svg class="layer" width="1200" height="2120" viewBox="0 0 1200 2120">
    <defs>
      <linearGradient id="skin" x1="0" y1="0" x2="1" y2="0.3">
        <stop offset="0" stop-color="var(--skin-light)"/>
        <stop offset="0.55" stop-color="var(--skin-mid)"/>
        <stop offset="0.85" stop-color="var(--skin-dark)"/>
        <stop offset="1" stop-color="#1a1210"/>
      </linearGradient>
    </defs>
    <rect class="hero-photo" x="0" y="640" width="1200" height="1480" fill="url(#skin)" role="img" aria-label="Close-up photo of a model's eye wearing dramatic eyelash extensions"/>
    <path class="swoosh-black" d="M350 800 C700 760 1000 740 1200 880 V1180 C1020 900 700 820 350 800 Z" fill="var(--ink)"/>
    <path class="swoosh-coral" d="M0 690 C60 760 160 810 320 800 C600 780 1000 720 1200 920 V880 C1000 700 600 720 300 760 C150 780 50 720 0 660 Z" fill="var(--coral)"/>
    <path class="header-white" d="M0 0 H1200 V880 C1000 700 600 720 300 760 C150 780 50 720 0 660 Z" fill="var(--white)"/>
  </svg>

  <div class="brand-name">Velvet Lash</div>
  <h1 class="headline"><span class="accent">EYELASH</span><span class="main">EXTENSIONS</span></h1>

  <div class="product-band"></div>
  <div class="product" style="left:89px">
    <div class="product-tile"><div class="product-shot" role="img" aria-label="Tray of 7-ply lash flares"></div></div>
    <div class="product-name">Eyelash7ply</div>
  </div>
  <div class="product" style="left:433px">
    <div class="product-tile"><div class="product-shot" role="img" aria-label="Tray of 12-ply lash flares"></div></div>
    <div class="product-name">Eyelash12ply</div>
  </div>
  <div class="product" style="left:777px">
    <div class="product-tile"><div class="product-shot" role="img" aria-label="Tray of 15-ply lash flares"></div></div>
    <div class="product-name">Eyelash15ply</div>
  </div>

  <!-- footer band -->
  <svg class="layer" width="1200" height="4000" viewBox="0 0 1200 4000" style="top:0">
    <rect class="footer-black" x="0" y="3400" width="1200" height="600" fill="var(--ink)"/>
    <path class="footer-coral" d="M0 3850 C60 3790 160 3720 320 3690 C520 3650 1000 3730 1200 3440 V3400 C1000 3690 500 3610 300 3650 C150 3690 50 3760 0 3820 Z" fill="var(--coral)"/>
    <path class="features-white" d="M0 2410 H1200 V3400 C1000 3690 500 3610 300 3650 C150 3690 50 3760 0 3820 Z" fill="var(--white)"/>
  </svg>

  <section class="features">
    <div class="feature" style="top:2550px">
      <svg class="feature-icon" viewBox="0 0 150 150" fill="none" stroke="var(--ink)" stroke-width="4" stroke-linecap="round">
        <circle cx="75" cy="75" r="71"/>
        <path d="M28 72 Q45 86 60 72 M90 72 Q105 86 122 72"/>
        <path d="M34 80 L30 88 M44 83 L43 92 M54 80 L57 88 M96 80 L93 88 M106 83 L107 92 M116 80 L120 88"/>
      </svg>
      <div class="feature-text">
        <div class="feature-title">Professional Falsies</div>
        <div class="feature-desc">Create beautiful and eye-opening appearances</div>
      </div>
    </div>
    <div class="feature" style="top:2815px">
      <svg class="feature-icon" viewBox="0 0 150 150" fill="none" stroke="var(--ink)" stroke-width="4" stroke-linecap="round">
        <circle cx="75" cy="75" r="71"/>
        <path d="M40 55 Q75 35 110 58"/>
        <path d="M38 85 Q70 100 112 78"/>
        <path d="M50 90 L44 100 M62 94 L60 105 M76 94 L78 105 M90 90 L95 100"/>
      </svg>
      <div class="feature-text">
        <div class="feature-title">Long-Lasting</div>
        <div class="feature-desc">Delicate overlapping hairs create the most authentic look</div>
      </div>
    </div>
    <div class="feature" style="top:3080px">
      <svg class="feature-icon" viewBox="0 0 150 150" fill="none" stroke="var(--ink)" stroke-width="4" stroke-linecap="round">
        <circle cx="75" cy="75" r="71"/>
        <path d="M35 70 Q75 40 115 70 Q75 95 35 70 Z"/>
        <circle cx="75" cy="68" r="11" fill="var(--ink)"/>
        <path d="M40 120 L70 90"/>
      </svg>
      <div class="feature-text">
        <div class="feature-title">Handmade Perfection</div>
        <div class="feature-desc">Individually hand made with extreme attention to detail</div>
      </div>
    </div>
    <div class="feature" style="top:3345px">
      <svg class="feature-icon" viewBox="0 0 150 150" fill="none" stroke="var(--ink)" stroke-width="4" stroke-linecap="round">
        <circle cx="75" cy="75" r="71"/>
        <path d="M75 115 L55 40 M75 115 L65 35 M75 115 L75 32 M75 115 L85 35 M75 115 L95 40"/>
      </svg>
      <div class="feature-text">
        <div class="feature-title">Knot-Free Flares</div>
        <div class="feature-desc">Each tray holds 56 individual flares with a dramatic C-Curl</div>
      </div>
    </div>
  </section>

  <div class="pack-info">
    <span><span class="num">100</span> TRAYS/BOX</span>
    <span><span class="num">12</span> BOXES/CASE</span>
  </div>

</main>
</body>
</html>
```